Rocket business card

Modern business card design, use of color is good with clean space too.

Things to include on card:

Quote: I add fuel to your optometry practice

- Eyewear Sales
- Admin Duties
- Revenue Collection
- Leadership
- Tech Adoption
- COGS Reduction
- Product Sourcing
-Medical Growth

Dalton Vessey, CEO
Glint Harbor
Text Me! 847-302-1964
dalton@glintharbor.example

```html
<!DOCTYPE html>
<html lang="en">
<head>
<meta charset="utf-8">
<title>Glint Harbor Business Card</title>
<link rel="stylesheet" href="https://fonts.googleapis.com/css2?family=Roboto:wght@400;700&display=swap">
<style>
  :root {
    --backdrop: #1c1c1e;
    --card-white: #fbfbfb;
    --ink: #1f1f1f;
    --accent-red: #dc3a2e;
    --grad-start: #d9362f;
    --grad-mid: #e86a28;
    --grad-end: #f6a11f;
    --on-orange: #ffffff;
  }
  * { box-sizing: border-box; margin: 0; padding: 0; }
  html, body {
    width: 1200px;
    height: 1004px;
    overflow: hidden;
    background: var(--backdrop);
    font-family: "Roboto", sans-serif;
  }
  .sheet {
    width: 1200px;
    height: 1004px;
    display: flex;
    flex-direction: column;
    align-items: center;
    justify-content: center;
    gap: 44px;
  }
  .card {
    position: relative;
    width: 700px;
    height: 400px;
    border-radius: 4px;
    overflow: hidden;
  }
  .card-front { background: var(--card-white); color: var(--ink); }
  .card-back {
    background: linear-gradient(135deg, var(--grad-start) 0%, var(--grad-mid) 50%, var(--grad-end) 100%);
    color: var(--on-orange);
    display: flex;
    flex-direction: column;
    align-items: center;
    justify-content: center;
    padding: 0 40px;
  }
  .wordmark {
    font-weight: 400;
    letter-spacing: 0.04em;
    text-transform: uppercase;
    line-height: 1;
  }
  .card-front .wordmark {
    position: absolute;
    left: 44px;
    top: 56px;
    font-size: 32px;
    color: var(--ink);
  }
  .contact {
    position: absolute;
    left: 44px;
    top: 178px;
    font-size: 18px;
    line-height: 1.4;
  }
  .contact-name {
    font-size: 27px;
    font-weight: 700;
    color: var(--accent-red);
    margin-bottom: 4px;
  }
  .text-me { color: var(--accent-red); font-weight: 700; }
  .accent-disc {
    position: absolute;
    right: 28px;
    top: 40px;
    width: 330px;
    height: 330px;
    border-radius: 50%;
    background: linear-gradient(135deg, var(--grad-start) 0%, var(--grad-mid) 50%, var(--grad-end) 100%);
  }
  .card-back .wordmark { font-size: 56px; }
  .website {
    margin-top: 16px;
    font-size: 20px;
    letter-spacing: 0.08em;
  }
  .quote {
    margin-top: 30px;
    font-size: 19px;
    font-weight: 700;
    text-align: center;
  }
  .services {
    margin-top: 16px;
    list-style: none;
    display: grid;
    grid-template-columns: repeat(4, auto);
    column-gap: 28px;
    row-gap: 8px;
    font-size: 15px;
    text-align: center;
  }
</style>
</head>
<body>
  <main class="sheet">
    <section class="card card-front">
      <div class="wordmark">Glint Harbor</div>
      <div class="contact">
        <p class="contact-name">Dalton Vessey</p>
        <p class="contact-title">CEO, Glint Harbor</p>
        <p class="contact-phone"><span class="text-me">Text Me!</span> 847-302-1964</p>
        <p class="contact-email">dalton@glintharbor.example</p>
      </div>
      <div class="accent-disc" role="img" aria-label="Rocket illustration on an orange gradient disc"></div>
    </section>

    <section class="card card-back">
      <div class="wordmark">Glint Harbor</div>
      <p class="website">www.glintharbor.example</p>
      <p class="quote">“I add fuel to your optometry practice”</p>
      <ul class="services">
        <li>Eyewear Sales</li>
        <li>Admin Duties</li>
        <li>Revenue Collection</li>
        <li>Leadership</li>
        <li>Tech Adoption</li>
        <li>COGS Reduction</li>
        <li>Product Sourcing</li>
        <li>Medical Growth</li>
      </ul>
    </section>
  </main>
</body>
</html>
```